Designing a front label called Ice Secco / Bottle Label for a Sparkling Wine called Secco Ice

We want to bring a Secco Ice on the market. For this we need a front label. Bottle is painted white and the capsule is fixed. (Black with golden lettering K.Wendlicher) Height of label max. 8.5cm. The whole thing should be fresh teen. Happy with reference to Ice .... etc. Secco is the German version of Prosecco. But better. There are currently many Secco Ice on the market. We also want one now. www.wendlicher.de We have a nice white lacquered TRV bottle with capsule. it just fehtl the right label. Sender K.Wendlicher does not have to be on top ... but if it fits. Lettering is already in the capsule anyway.

Target Market(s)

Supermarket, gals, party, alcohol, RRP 4.99 €

Font styles to use
Decorative

Colors

Requirements
Must have
• Self-adhesive label, printable data in 4c, reference to ice, black, golden reference to the capsule.
Nice to have
• Ice cubes, cool, cool.
Should not have
• boredom

```html
<!DOCTYPE html>
<html lang="en">
<head>
<meta charset="utf-8">
<title>Secco Ice – Front Label</title>
<link href="https://fonts.googleapis.com/css2?family=Great+Vibes&family=Uncial+Antiqua&family=Cormorant+Garamond:wght@500;600&display=swap" rel="stylesheet">
<style>
  :root {
    --stage: #6b6b6b;
    --label-black: #000000;
    --frost-white: #f7fafd;
    --frost-pale: #dfeaf5;
    --frost-blue: #a9c4e2;
    --gold-light: #f7d77a;
    --gold: #e0a93a;
    --gold-deep: #b8801f;
    --gold-flat: #dcaa48;
  }
  html, body {
    margin: 0;
    padding: 0;
    width: 1200px;
    height: 1200px;
    overflow: hidden;
    background: var(--stage);
  }
  .canvas {
    position: relative;
    width: 1200px;
    height: 1200px;
  }
  .label {
    position: absolute;
    left: 175px;
    top: 30px;
    width: 852px;
    height: 1140px;
    overflow: hidden;
  }
  .frost-border {
    position: absolute;
    inset: 0;
    background:
      radial-gradient(circle at 12% 6%, var(--frost-white) 0, transparent 14%),
      radial-gradient(circle at 40% 3%, var(--frost-blue) 0, transparent 9%),
      radial-gradient(circle at 70% 5%, var(--frost-white) 0, transparent 12%),
      radial-gradient(circle at 95% 30%, var(--frost-blue) 0, transparent 10%),
      radial-gradient(circle at 3% 45%, var(--frost-blue) 0, transparent 10%),
      radial-gradient(circle at 4% 80%, var(--frost-white) 0, transparent 12%),
      radial-gradient(circle at 96% 70%, var(--frost-white) 0, transparent 12%),
      radial-gradient(circle at 30% 97%, var(--frost-blue) 0, transparent 10%),
      radial-gradient(circle at 65% 96%, var(--frost-white) 0, transparent 12%),
      radial-gradient(circle at 88% 97%, var(--frost-blue) 0, transparent 9%),
      linear-gradient(135deg, var(--frost-white), var(--frost-pale) 40%, var(--frost-blue) 60%, var(--frost-white));
  }
  .label-field {
    position: absolute;
    left: 48px;
    top: 56px;
    right: 44px;
    bottom: 60px;
    background: var(--label-black);
    border-radius: 36px;
    box-shadow: 0 0 10px 6px var(--label-black);
  }
  .house-mark {
    position: absolute;
    left: 0;
    right: 0;
    top: 170px;
    display: flex;
    justify-content: center;
    align-items: center;
    gap: 14px;
    font-family: "Cormorant Garamond", serif;
    font-weight: 600;
    font-size: 34px;
    color: var(--gold-flat);
  }
  .house-mark .dot {
    width: 18px;
    height: 18px;
    border-radius: 50%;
    background: var(--gold-flat);
  }
  .producer {
    position: absolute;
    left: 0;
    right: 0;
    top: 290px;
    text-align: center;
    font-family: "Great Vibes", cursive;
    font-size: 76px;
    line-height: 1;
    color: var(--gold-flat);
  }
  .divider {
    position: absolute;
    left: 255px;
    top: 388px;
    width: 342px;
    height: 16px;
  }
  .product-name {
    position: absolute;
    left: 0;
    right: 0;
    top: 500px;
    margin: 0;
    text-align: center;
    font-family: "Uncial Antiqua", serif;
    font-weight: 400;
    font-size: 150px;
    line-height: 160px;
    background: linear-gradient(90deg, var(--gold-deep), var(--gold-light) 35%, var(--gold) 65%, var(--gold-deep));
    -webkit-background-clip: text;
    background-clip: text;
    color: transparent;
  }
  .product-name span { display: block; }
  .net-volume {
    position: absolute;
    left: 0;
    right: 0;
    top: 990px;
    text-align: center;
    font-family: "Cormorant Garamond", serif;
    font-weight: 500;
    font-size: 40px;
    word-spacing: 6px;
    font-variant-numeric: lining-nums;
    color: var(--gold-flat);
  }
</style>
</head>
<body>
  <main class="canvas">
    <section class="label">
      <div class="frost-border" role="img" aria-label="Frosted border of white and pale blue snowflakes framing the label"></div>
      <div class="label-field"></div>

      <div class="house-mark"><span class="dot"></span>K.Wendlicher</div>

      <div class="producer">K.Wendlicher</div>

      <svg class="divider" viewBox="0 0 342 16" aria-hidden="true">
        <line x1="0" y1="8" x2="150" y2="8" stroke="#dcaa48" stroke-width="1.5"/>
        <circle cx="171" cy="8" r="4" fill="#dcaa48"/>
        <line x1="192" y1="8" x2="342" y2="8" stroke="#dcaa48" stroke-width="1.5"/>
      </svg>

      <h1 class="product-name"><span>Secco</span><span>Ice</span></h1>

      <div class="net-volume">Net wt.1fl oz</div>
    </section>
  </main>
</body>
</html>
```